Trifold Leaflet - Osteopathy

Trifold Leaflet (A4 size paper) to provide information and promote an established English seafront osteopathy clinic.
I would like a simple modern design to reflect the seafront location and the caring nature of osteopathy treatment. The design needs to be not be generic or too corporate.
At the top of the front page in a large font should be the word "Osteopathy" as it will be displayed in a rack of leaflets (photo attached) and needs to be eye-catching.
I have attached a logo file and some examples of the kinds of designs that I like- but i'm very open to your expert ideas!
Also attached is a photo of the location- a bit of an ugly building but right on the beach, it would be great if this location could be emphasized!
The Word files: Leaflets word-inside.doc & Leaflets word-outside.doc uploaded show the content that I'd like- this is definitely not set in stone and I appreciate that less content is probably needed. Feel free to include/leave out whatever you feel is right.
More info on the practice can be found on my website:
www.harrowdenbackcare.com
The shutterstock images are ones that I have previously bought the rights to use, but only use them if you think they suit you design- I have included them i case they are of use to you.
Target Market(s)
Any adult.
Industry/Entity Type
Building
Look and feel
Each slider illustrates characteristics of the customer's brand and the style your logo design should communicate.

```html
<!DOCTYPE html>
<html lang="en">
<head>
<meta charset="utf-8">
<title>Harrowden Osteopathy – Trifold Leaflet</title>
<link href="https://fonts.googleapis.com/css2?family=Open+Sans:wght@400;600&family=Anton&display=swap" rel="stylesheet">
<style>
  :root{
    --red:#e3232b;
    --charcoal:#3a3a3c;
    --ink:#444446;
    --paper:#ffffff;
    --backdrop:#e6e6e6;
    --sea:#5fc6cf;
    --sky:#8fc3e6;
    --sand:#e9e2d6;
    --skin:#c99a7c;
  }
  *{box-sizing:border-box;margin:0;padding:0}
  html,body{width:1200px;height:1200px;overflow:hidden}
  body{background:var(--backdrop);font-family:"Open Sans",Arial,sans-serif;color:var(--ink);position:relative}
  .panel{position:absolute;top:130px;width:460px;height:940px;background:var(--paper);overflow:hidden;box-shadow:0 6px 18px rgba(0,0,0,.18)}
  .panel--front{left:90px}
  .panel--inside{left:650px}
  .panel__art{position:absolute;inset:0}
  .brand{position:absolute;font-family:"Open Sans",Arial,sans-serif;font-weight:400;color:var(--red);white-space:nowrap}
  .panel--front .brand{top:70px;left:40px;font-size:33px}
  .panel--inside .brand{right:28px;bottom:40px;font-size:20px}
  .services{position:absolute;top:138px;left:40px;width:260px;font-size:14px;line-height:1.5;color:#555}
  .services .quote{color:var(--red);font-weight:600;font-size:20px;line-height:0}
  .slogan{position:absolute;top:610px;left:120px;transform:rotate(-10deg);transform-origin:left top}
  .slogan__main{font-family:"Anton",Impact,sans-serif;font-size:44px;color:var(--red);letter-spacing:1px;-webkit-text-stroke:1.5px #fff;line-height:1}
  .slogan__words{font-family:"Anton",Impact,sans-serif;font-size:22px;color:#fff;text-shadow:0 1px 3px rgba(0,0,0,.5);line-height:1.05}
  .slogan__words span{display:block}
  .slogan__words span:nth-child(2){margin-left:55px}
  .slogan__words span:nth-child(3){margin-left:110px}
  .contact{position:absolute;left:40px;bottom:34px;font-size:12px;line-height:1.45;color:#333;font-style:normal}
  .contact__venue{color:var(--red);font-size:15px;margin-bottom:4px}
  .contact__phone{display:flex;align-items:center;gap:5px}
  .contact__web{margin-top:4px}
  .portrait{position:absolute;top:180px;right:40px;width:130px;height:126px;border:1px solid var(--red);padding:6px;background:#fff}
  .portrait div{width:100%;height:100%;background:linear-gradient(160deg,#d9d4cf,#f2f0ee)}
  .practitioner{position:absolute;top:318px;right:40px;text-align:right}
  .practitioner__name{color:var(--red);font-size:22px}
  .practitioner__title{font-size:13px;color:#333}
  .bio{position:absolute;top:400px;left:40px;right:40px;font-size:14px;line-height:1.5;color:#333}
  .bio p{margin-bottom:18px}
</style>
</head>
<body>

<section class="panel panel--front" aria-label="Leaflet front panel">
  <svg class="panel__art" width="460" height="940" viewBox="0 0 460 940">
    <defs>
      <linearGradient id="beachTone" x1="0" y1="0" x2="0" y2="1">
        <stop offset="0" stop-color="var(--sky)"/>
        <stop offset=".4" stop-color="var(--sea)"/>
        <stop offset=".62" stop-color="var(--skin)"/>
        <stop offset="1" stop-color="var(--sand)"/>
      </linearGradient>
    </defs>
    <polygon points="460,150 40,590 400,940 460,940" fill="var(--red)" stroke="var(--red)" stroke-width="40" stroke-linejoin="round"/>
    <polygon points="460,200 110,585 460,880" fill="var(--charcoal)" stroke="var(--charcoal)" stroke-width="30" stroke-linejoin="round"/>
    <polygon points="460,250 135,600 460,860" fill="url(#beachTone)" role="img" aria-label="Photo: woman sitting on a sunny beach facing the turquoise sea"/>
  </svg>
  <div class="brand">Harrowden Osteopathy</div>
  <p class="services"><span class="quote">“</span> Arthritis &amp; Joint Pain Back &amp; Neck Pain Frozen Shoulder Cranial Tension Sports Injury Sciatica <span class="quote">”</span></p>
  <div class="slogan">
    <div class="slogan__main">RELIEVE PAIN</div>
    <div class="slogan__words"><span>GENTLY</span><span>SAFELY</span><span>EFFECTIVELY</span></div>
  </div>
  <address class="contact">
    <div class="contact__venue">The Shoreline Fitness Centre</div>
    <div>Seafront, Marine Parade,</div>
    <div>Harrowden HN4 2QT</div>
    <div class="contact__phone"><svg width="12" height="12" viewBox="0 0 24 24"><circle cx="12" cy="12" r="11" fill="none" stroke="#333" stroke-width="2"/><path d="M8 6l2 0 1 3-1.5 1a7 7 0 0 0 4 4l1-1.5 3 1v2c0 1-1 1.5-2 1.5A10 10 0 0 1 7 8c0-1 .5-2 1-2z" fill="#333"/></svg>01632 960418</div>
    <div class="contact__web">www.harrowdenbackcare.com</div>
  </address>
</section>

<section class="panel panel--inside" aria-label="Leaflet inside panel">
  <svg class="panel__art" width="460" height="940" viewBox="0 0 460 940">
    <defs>
      <linearGradient id="seafrontTone" x1="0" y1="0" x2="0" y2="1">
        <stop offset="0" stop-color="#6aa6d8"/>
        <stop offset=".5" stop-color="#b9c4cc"/>
        <stop offset=".75" stop-color="#9a9088"/>
        <stop offset="1" stop-color="#c9bba9"/>
      </linearGradient>
    </defs>
    <polygon points="0,0 360,0 0,410" fill="var(--red)"/>
    <polygon points="0,0 330,0 0,372" fill="var(--charcoal)"/>
    <polygon points="0,0 300,0 0,334" fill="url(#seafrontTone)" role="img" aria-label="Photo: the clinic building on the seafront beside the pebble beach"/>
  </svg>
  <div class="portrait" role="img" aria-label="Portrait photo of the osteopath"><div></div></div>
  <div class="practitioner">
    <div class="practitioner__name">Tom Ellery</div>
    <div class="practitioner__title">BOst. (hons)</div>
  </div>
  <div class="bio">
    <p>Tom Ellery is an experienced Harrowden osteopath, treating a wide variety of joint, muscle and nerve problems. In addition to general osteopathic treatment of back pain and neck pain, he has particular experience in shoulder conditions &amp; cranial osteopathy. He treats a wide variety of patients from babies to the elderly. Tom is able to offer advice on general &amp; work-based posture, together with individual exercise programmes for rehabilitation for a wide variety of problems.</p>
    <p>Tom is registered with the Osteopathic Practice Register, a member of the Coastal Osteopathic Society and is trained in the Harlow Release Technique of frozen shoulder rehabilitation.</p>
    <p>For further information, or to book an appointment, please call the Shoreline Fitness Centre or visit: www.harrowdenbackcare.com</p>
  </div>
  <address class="contact">
    <div class="contact__venue">The Shoreline Fitness Centre</div>
    <div>Seafront, Marine Parade,</div>
    <div>Harrowden HN4 2QT</div>
    <div class="contact__phone"><svg width="12" height="12" viewBox="0 0 24 24"><circle cx="12" cy="12" r="11" fill="none" stroke="#333" stroke-width="2"/><path d="M8 6l2 0 1 3-1.5 1a7 7 0 0 0 4 4l1-1.5 3 1v2c0 1-1 1.5-2 1.5A10 10 0 0 1 7 8c0-1 .5-2 1-2z" fill="#333"/></svg>01632 960418</div>
    <div class="contact__web">www.harrowdenbackcare.com</div>
  </address>
  <div class="brand">Harrowden Osteopathy</div>
</section>

</body>
</html>
```